Business Card Design Project

We need a logo design for a new company based in Southern California called "Norvale Security Services, Inc." We install security and camera systems for homeowners and business, to protect their assets.
Updates

Project Deadline Extended
Reason: LOGO Design completes in eight days. Would like that design decided before we finish the business cards. Thanks...

Target Market(s)

Homeowners and business owners looking for additional protection of their assets.

Industry/Entity Type

Security

Font styles to use
Serif

Requirements
Must have
• Company Name
Office# 909-472-3615
Service# 909-472-3616
email: NorvaleSecurity@brimwell.net
address: 48620 Thorncrest Lane Rancho Cucamonga, CA 91704
Nice to have
• Serving Southern California

```html
<!DOCTYPE html>
<html lang="en">
<head>
<meta charset="utf-8">
<title>Norvale Security Services, Inc. – Business Card</title>
<link rel="stylesheet" href="https://fonts.googleapis.com/css2?family=Tinos&display=swap">
<style>
  :root {
    --card-bg: #ffffff;
    --ink: #111111;
    --sage: #a5bd7c;
    --sage-text: #8fac63;
    --camera-light: #e6e6e6;
    --camera-dark: #8a8a8a;
  }
  html, body {
    margin: 0;
    padding: 0;
    overflow: hidden;
    background: var(--card-bg);
  }
  .card {
    position: relative;
    width: 1200px;
    height: 740px;
    background: var(--card-bg);
    font-family: "Tinos", "Times New Roman", serif;
    color: var(--ink);
    overflow: hidden;
  }
  .name-band {
    position: absolute;
    left: 43px;
    top: 8px;
    width: 1133px;
    height: 147px;
    background: var(--sage);
    display: flex;
    align-items: center;
    justify-content: center;
  }
  .company-name {
    margin: 0;
    font-weight: 400;
    font-size: 72px;
    line-height: 1;
    white-space: nowrap;
  }
  .email {
    position: absolute;
    left: 0;
    width: 1200px;
    top: 160px;
    text-align: center;
    font-size: 37px;
  }
  .camera-art {
    position: absolute;
    left: 48px;
    top: 245px;
    width: 245px;
    height: 230px;
    border-radius: 14px;
    background: linear-gradient(135deg, var(--camera-light), var(--camera-dark));
  }
  .phones {
    position: absolute;
    left: 338px;
    top: 285px;
    font-size: 49px;
    line-height: 60px;
  }
  .phones p { margin: 0; }
  .address {
    position: absolute;
    left: 0;
    width: 1200px;
    top: 500px;
    margin: 0;
    text-align: center;
    font-size: 38px;
    line-height: 62px;
    font-style: normal;
    padding-right: 20px;
    box-sizing: border-box;
  }
  .rule {
    position: absolute;
    left: 43px;
    width: 1133px;
    height: 3px;
    top: 638px;
    background: var(--ink);
  }
  .tagline {
    position: absolute;
    left: 43px;
    width: 1133px;
    top: 648px;
    text-align: center;
    font-size: 52px;
    letter-spacing: 0.2em;
    color: var(--sage-text);
    white-space: nowrap;
  }
  .base-rule {
    position: absolute;
    left: 43px;
    width: 1133px;
    height: 4px;
    top: 724px;
    background: var(--sage);
  }
</style>
</head>
<body>
  <main class="card">
    <header class="name-band">
      <h1 class="company-name">Norvale Security Services, Inc.</h1>
    </header>
    <div class="email">Email: NorvaleSecurity@brimwell.net</div>
    <div class="camera-art" role="img" aria-label="Wall-mounted security camera illustration"></div>
    <div class="phones">
      <p class="phone-office">Office: 909-472-3615</p>
      <p class="phone-service">Service: 909-472-3616</p>
    </div>
    <address class="address">Address: 48620 Thorncrest Lane Rancho Cucamonga,<br>CA 91704</address>
    <div class="rule"></div>
    <div class="tagline">Serving Southern California</div>
    <div class="base-rule"></div>
  </main>
</body>
</html>
```